Hadley & Partners, LLC Business Card 2016

We need a new business card design for a very important trade show coming up.

We are a compliance Consulting Firm. Our clients are stock brokerage firms and investment advisers.

I would like our logo on both sides of the card.

Info in the front of the card shold include:

Logo
First & Last Name
Title
Office #
Cell #
Email
Company Address (42 W. Calloway St., Suite 300 Brookvale, CA 91417

Back of the card should include the logo and url: www.hadleypartnersgroup.com

Target Market(s)

Stock Brokerage Firms and Investment Advisers

Industry/Entity Type

Financial Service

Contact Information for Business Card

Marcus J. Pellew
President
42 W. Calloway St., Suite 300
Brookvale, CA 91417
O 555.210.0147 ext. 204
C 555.340.0193
Email: marcus@hadleypartnersgroup.com
www.hadleypartnersgroup.com

Requirements
Nice to have
• The back of the card could be black with the logo with the white letters.
• I do want the front of the card to at least have the color logo with the black "Hadley & Partners Lettering.

```html
<!DOCTYPE html>
<html lang="en">
<head>
<meta charset="utf-8">
<title>Hadley &amp; Partners — Business Card</title>
<link rel="stylesheet" href="https://fonts.googleapis.com/css2?family=Marcellus+SC&display=swap">
<style>
  :root {
    --backdrop: #9a5a30;
    --card: #262626;
    --card-edge: #1c1c1c;
    --silver: #d9d9d9;
    --silver-dim: #bdbdbd;
    --text: #ececec;
    --accent-red: #c4161c;
    --rule: #cfcfcf;
  }
  * { margin: 0; padding: 0; box-sizing: border-box; }
  html, body { width: 1200px; height: 1000px; overflow: hidden; }
  body {
    position: relative;
    background: var(--backdrop);
    font-family: "Marcellus SC", serif;
    color: var(--text);
  }
  .card {
    position: absolute;
    top: 30px;
    width: 514px;
    height: 856px;
    border-radius: 22px;
    background: radial-gradient(ellipse at 50% 40%, #2d2d2d 0%, var(--card) 60%, var(--card-edge) 100%);
    text-align: center;
  }
  .card--back { left: 44px; }
  .card--front { left: 646px; }

  .brand-mark {
    position: absolute;
    left: 50%;
    width: 44px;
    height: 44px;
    margin-left: -22px;
    background: var(--silver-dim);
  }
  .brand-name {
    position: absolute;
    left: 0; right: 0;
    font-size: 38px;
    line-height: 44px;
    letter-spacing: 2px;
    color: var(--silver);
    white-space: nowrap;
  }
  .card--back .brand-mark { top: 206px; }
  .card--back .brand-name { top: 348px; }
  .card--front .brand-mark { top: 76px; }
  .card--front .brand-name { top: 200px; }

  .tagline {
    position: absolute;
    top: 573px; left: 0; right: 0;
    font-size: 22px;
    line-height: 29px;
    letter-spacing: 1.5px;
  }
  .rule {
    position: absolute;
    height: 1px;
    background: var(--rule);
  }
  .card--back .rule--left { top: 615px; left: 0; width: 134px; }
  .card--back .rule--right { top: 615px; right: 0; width: 124px; }

  .website {
    position: absolute;
    top: 787px; left: 0; right: 0;
    font-size: 17px;
    letter-spacing: 2px;
  }

  .person-name {
    position: absolute;
    top: 351px; left: 0; right: 0;
    font-size: 32px;
    line-height: 53px;
    letter-spacing: 5px;
    color: var(--silver);
  }
  .person-title {
    position: absolute;
    top: 458px; left: 0; right: 0;
    font-size: 22px;
    line-height: 28px;
    letter-spacing: 4px;
    color: var(--accent-red);
  }
  .contact {
    position: absolute;
    top: 633px; left: 0; right: 0;
    font-size: 14px;
    line-height: 19px;
    letter-spacing: 1.5px;
  }
  .contact li { list-style: none; }
  .contact .spaced { margin-top: 4px; }
  .card--front .rule--left { top: 682px; left: 0; width: 74px; }
  .card--front .rule--right { top: 682px; right: 0; width: 80px; }
</style>
</head>
<body>
  <section class="card card--back">
    <div class="brand-mark"></div>
    <div class="brand-name">HADLEY &amp; PARTNERS</div>
    <p class="tagline">Trusted<br>Compliance<br>Partners</p>
    <span class="rule rule--left"></span>
    <span class="rule rule--right"></span>
    <p class="website">WWW.HADLEYPARTNERSGROUP.COM</p>
  </section>

  <section class="card card--front">
    <div class="brand-mark"></div>
    <div class="brand-name">HADLEY &amp; PARTNERS</div>
    <p class="person-name">Marcus J.<br>Pellew</p>
    <p class="person-title">PRESIDENT</p>
    <ul class="contact">
      <li>42 W. Calloway St., Suite 300</li>
      <li>Brookvale, CA 91417</li>
      <li>office: 555.210.0147 ext. 204</li>
      <li class="spaced">mobile: 555.340.0193</li>
      <li class="spaced">marcus@hadleypartnersgroup.com</li>
    </ul>
    <span class="rule rule--left"></span>
    <span class="rule rule--right"></span>
  </section>
</body>
</html>
```